Flip Book Reference Guide for Medical Offices

We are looking to take a PowerPoint presentation and turn it into a flip book for our front office staff to use as a quick reference when needed. We are hoping for someone to take a quick once over of the PowerPoint then take it to the next level and make it look beautiful and professional. Alignment, graphics and clarity of design can make or break these sorts of products… we have the message, now need to ensure it's received and that is where you will come into play.

Industry/Entity Type

Medical

```html
<!DOCTYPE html>
<html lang="en">
<head>
<meta charset="utf-8">
<title>Morning Tasks – Front Office Reference</title>
<link rel="stylesheet" href="https://fonts.googleapis.com/css2?family=Montserrat:ital,wght@0,300;0,400;0,500;0,700;1,400;1,700&display=swap">
<style>
  :root {
    --orange: #f28a1e;
    --orange-deep: #e4581f;
    --red: #d9341f;
    --yellow: #f5b324;
    --blue: #0b6fa8;
    --teal: #1aa0c8;
    --navy: #0d3a5c;
    --heading: #2c5577;
    --text: #2b2b2b;
    --muted: #5a5a5a;
    --paper: #f4f4f4;
    --white: #ffffff;
  }
  * { margin: 0; padding: 0; box-sizing: border-box; }
  html, body { width: 1200px; height: 900px; overflow: hidden; background: var(--white); }
  .slide {
    position: relative;
    width: 1200px;
    height: 900px;
    overflow: hidden;
    font-family: "Montserrat", Arial, sans-serif;
    color: var(--text);
  }
  .backdrop {
    position: absolute;
    inset: 0;
    background: radial-gradient(ellipse at 70% 45%, #e2e2e2 0%, #eeeeee 40%, #f8f8f8 75%);
  }
  .bands { position: absolute; inset: 0; }
  .title {
    position: absolute;
    left: 110px;
    top: 138px;
    font-size: 71px;
    font-weight: 300;
    color: var(--heading);
    letter-spacing: -0.5px;
  }
  .title strong { font-weight: 700; color: var(--orange); }
  .tasks { position: absolute; left: 99px; top: 0; list-style: none; }
  .task {
    position: absolute;
    left: 0;
    width: 1050px;
    display: flex;
    align-items: flex-start;
  }
  .task-icon { width: 48px; height: 48px; flex: none; }
  .task-body { margin-left: 28px; font-size: 24px; line-height: 1.3; }
  .task-body b { font-weight: 700; }
  .task-body .hint { font-style: italic; font-weight: 400; font-size: 22px; }
  .deadline { color: var(--heading); font-style: italic; font-weight: 700; font-size: 23.5px; }
  .detail { color: var(--muted); font-size: 22.5px; }
  .chev { color: var(--orange); font-weight: 700; margin: 0 6px; }
  .brand {
    position: absolute;
    right: 52px;
    bottom: 62px;
    display: flex;
    align-items: center;
    gap: 12px;
    color: var(--white);
    font-size: 36px;
    font-weight: 700;
  }
  .brand-dot { width: 22px; height: 22px; border-radius: 50%; background: var(--white); }
</style>
</head>
<body>
<main class="slide">
  <div class="backdrop" role="img" aria-label="Softly blurred office desk with a coffee mug and keyboard"></div>

  <svg class="bands" width="1200" height="900" viewBox="0 0 1200 900" aria-hidden="true">
    <defs>
      <linearGradient id="top-band" x1="0" y1="0" x2="1" y2="0">
        <stop offset="0" stop-color="var(--blue)"/>
        <stop offset="0.35" stop-color="var(--teal)"/>
        <stop offset="0.6" stop-color="var(--navy)"/>
        <stop offset="1" stop-color="var(--yellow)"/>
      </linearGradient>
      <linearGradient id="bottom-left" x1="0" y1="0" x2="1" y2="1">
        <stop offset="0" stop-color="var(--teal)"/>
        <stop offset="1" stop-color="var(--navy)"/>
      </linearGradient>
      <linearGradient id="bottom-right" x1="0" y1="0" x2="1" y2="0">
        <stop offset="0" stop-color="var(--yellow)"/>
        <stop offset="0.45" stop-color="var(--orange)"/>
        <stop offset="1" stop-color="var(--red)"/>
      </linearGradient>
    </defs>
    <polygon points="0,0 1200,0 1200,120 1020,60 760,10 300,40 0,70" fill="url(#top-band)"/>
    <polygon points="960,0 1200,0 1200,190 1110,90" fill="var(--yellow)" opacity="0.9"/>
    <polygon points="0,680 240,720 420,900 0,900" fill="url(#bottom-left)"/>
    <polygon points="300,760 560,830 640,900 360,900" fill="var(--blue)" opacity="0.85"/>
    <polygon points="520,900 760,720 1200,640 1200,900" fill="url(#bottom-right)"/>
    <polygon points="860,900 1040,780 1200,760 1200,900" fill="var(--orange-deep)" opacity="0.8"/>
  </svg>

  <h1 class="title">Morning <strong>Tasks</strong></h1>

  <ul class="tasks">
    <li class="task" style="top:253px">
      <svg class="task-icon" viewBox="0 0 48 48" aria-hidden="true"><circle cx="24" cy="24" r="24" fill="var(--orange)"/><rect x="14" y="13" width="20" height="22" rx="2" fill="none" stroke="var(--white)" stroke-width="2"/><text x="24" y="28" text-anchor="middle" font-size="9" font-weight="700" fill="var(--white)" font-family="Montserrat, sans-serif">BAT</text></svg>
      <p class="task-body"><b>Open a batch</b> <span class="hint">(01012016ChartLinkNameLocation)</span></p>
    </li>
    <li class="task" style="top:322px">
      <svg class="task-icon" viewBox="0 0 48 48" aria-hidden="true"><circle cx="24" cy="24" r="24" fill="var(--orange)"/><rect x="15" y="12" width="18" height="24" rx="1" fill="none" stroke="var(--white)" stroke-width="2"/><path d="M19 18h10M19 23h10M19 28h6" stroke="var(--white)" stroke-width="2"/></svg>
      <p class="task-body">Count &amp; <b>document petty cash</b></p>
    </li>
    <li class="task" style="top:400px">
      <svg class="task-icon" viewBox="0 0 48 48" aria-hidden="true"><circle cx="24" cy="24" r="24" fill="var(--orange)"/><rect x="13" y="14" width="22" height="20" rx="2" fill="none" stroke="var(--white)" stroke-width="2"/><path d="M13 20h22M18 11v5M30 11v5" stroke="var(--white)" stroke-width="2"/><circle cx="29" cy="29" r="5" fill="var(--orange)" stroke="var(--white)" stroke-width="2"/></svg>
      <p class="task-body">Encounter Upload Deadline<br>
        <span class="deadline">ALL encounters for previous day MUST be verified and uploaded by 9:00am</span><br>
        <span class="detail">E&amp;M code, DX, and provider signature on each page</span></p>
    </li>
    <li class="task" style="top:517px">
      <svg class="task-icon" viewBox="0 0 48 48" aria-hidden="true"><circle cx="24" cy="24" r="24" fill="var(--orange)"/><rect x="15" y="12" width="18" height="24" rx="2" fill="none" stroke="var(--white)" stroke-width="2"/><path d="M12 17h5M12 24h5M12 31h5M20 19h9M20 24h9M20 29h9" stroke="var(--white)" stroke-width="2"/></svg>
      <p class="task-body">Work unconfirmed appointment reminders – Dashboard<span class="chev">&gt;</span>Appointment Outreach</p>
    </li>
    <li class="task" style="top:591px">
      <svg class="task-icon" viewBox="0 0 48 48" aria-hidden="true"><circle cx="24" cy="24" r="24" fill="var(--orange)"/><path d="M14 13v21h21" fill="none" stroke="var(--white)" stroke-width="2"/><path d="M19 30v-5M24 30v-8M29 30v-11" stroke="var(--white)" stroke-width="3"/><path d="M18 21l6-5 4 3 5-5" fill="none" stroke="var(--white)" stroke-width="2"/></svg>
      <p class="task-body">Specialty Chart<span class="chev">&gt;</span>confirm referral or auth</p>
    </li>
  </ul>

  <div class="brand"><span class="brand-dot"></span><span>Evercrest Care</span></div>
</main>
</body>
</html>
```